Melissa Dorvan Personal Business Card

I like orange. It's would better if my card have an orange background
Address: 5820 Halvers Lane #417
San Jose
California
US
Tel: 4085172049

Industry/Entity Type

Business

```html
<!DOCTYPE html>
<html lang="en">
<head>
<meta charset="utf-8">
<title>Melissa Dorvan – Business Card</title>
<link rel="stylesheet" href="https://fonts.googleapis.com/css2?family=Cinzel:wght@500;600&family=Open+Sans:wght@400;700&display=swap">
<style>
  :root{
    --indigo:#3d3f96;
    --orange:#f08a2c;
    --peach:#f6cfb2;
    --peach-soft:#fbe7d8;
    --card:#ffffff;
    --shadow-grey:#d4d5d9;
    --ink:#2b2b2b;
    --backdrop:#ece9e4;
  }
  *{margin:0;padding:0;box-sizing:border-box}
  html,body{width:1200px;height:1020px;overflow:hidden;background:var(--backdrop)}
  .stage{width:1200px;height:1020px;display:flex;align-items:center;justify-content:center}
  .card{position:relative;width:1000px;height:570px;background:var(--card);
    box-shadow:0 10px 30px rgba(0,0,0,.18);overflow:hidden}
  .card-art{position:absolute;inset:0}
  .holder{position:absolute;left:40px;top:250px;color:#fff;font-family:"Open Sans",sans-serif}
  .holder-name{font-weight:700;font-size:34px;letter-spacing:.5px;line-height:1.1}
  .holder-role{font-size:22px;letter-spacing:1px;margin-top:4px}
  .brand{position:absolute;left:680px;top:130px;font-family:"Cinzel",serif;font-weight:600;
    font-size:50px;line-height:1;letter-spacing:2px;white-space:nowrap}
  .brand-first{color:var(--indigo);display:block}
  .brand-last{color:var(--orange);display:block;margin-left:40px;margin-top:6px}
  .contacts{position:absolute;left:40px;top:400px;list-style:none;font-family:"Open Sans",sans-serif;
    font-size:17px;color:var(--ink)}
  .contacts li{display:flex;align-items:center;gap:16px;height:38px}
  .contact-icon{width:30px;height:22px;background:var(--indigo);border-bottom:4px solid var(--orange);
    display:flex;align-items:center;justify-content:center}
  .contact-icon svg{width:12px;height:12px;fill:#fff}
</style>
</head>
<body>
<main class="stage">
  <section class="card" aria-label="Business card for Melissa Dorvan">
    <svg class="card-art" viewBox="0 0 1000 570" preserveAspectRatio="none" aria-hidden="true">
      <defs>
        <linearGradient id="peachFade" x1="0" y1="0" x2="1" y2="0">
          <stop offset="0" stop-color="#fff" stop-opacity="0"/>
          <stop offset="1" stop-color="#f6cfb2"/>
        </linearGradient>
        <linearGradient id="peachLow" x1="0" y1="0" x2="1" y2="0">
          <stop offset="0" stop-color="#fbe7d8"/>
          <stop offset="1" stop-color="#fff" stop-opacity="0"/>
        </linearGradient>
      </defs>
      <path class="band-right" d="M1000 0 H960 C820 160 790 380 830 570 H1000 Z" fill="url(#peachFade)"/>
      <path class="band-low" d="M0 380 H400 C520 375 585 330 600 250 C590 360 520 410 420 420 H0 Z" fill="url(#peachLow)"/>
      <path class="wave-shadow" d="M0 350 H385 C500 345 555 300 575 210 C570 320 510 370 400 378 H0 Z" fill="var(--shadow-grey)"/>
      <path class="wave-blue" d="M0 0 H760 C640 10 590 90 570 200 C550 300 500 340 380 350 H0 Z" fill="var(--indigo)"/>
      <path class="wave-line" d="M800 0 C670 15 615 95 592 205" fill="none" stroke="var(--orange)" stroke-width="7"/>
    </svg>

    <div class="holder">
      <p class="holder-name">ADRIAN VELLMORE</p>
      <p class="holder-role">GENERAL MANAGER</p>
    </div>

    <h1 class="brand"><span class="brand-first">Melissa</span><span class="brand-last">Dorvan</span></h1>

    <ul class="contacts">
      <li><span class="contact-icon"><svg viewBox="0 0 12 12"><path d="M2 1h3l1 3-2 1a7 7 0 0 0 3 3l1-2 3 1v3c-6 0-9-4-9-9z"/></svg></span>408 517 2049</li>
      <li><span class="contact-icon"><svg viewBox="0 0 12 12"><path d="M0 2h12v8H0z M1 3l5 4 5-4" stroke="#3d3f96" stroke-width="1"/></svg></span>melissa@dorvanstudio.com</li>
      <li><span class="contact-icon"><svg viewBox="0 0 12 12"><circle cx="6" cy="6" r="5.5"/></svg></span>www.dorvanstudio.com</li>
      <li><span class="contact-icon"><svg viewBox="0 0 12 12"><path d="M6 0a4 4 0 0 1 4 4c0 3-4 8-4 8S2 7 2 4a4 4 0 0 1 4-4z"/></svg></span>5820 Halvers Lane #417, San Jose, California</li>
    </ul>
  </section>
</main>
</body>
</html>
```